Lar Ferreirinha Banners Ads

We need to create 4 animated banners ads in GIF (3 arts for each banner) to Lar Ferreirinha Adwords Display Campaign
Lar Ferreirinha is an ecommerce in Brazil that sells high end home products.
It is a Branding Campaign, but we will add products images on it, so it has to be very sofisticated like the brand is.

We need 4 designs - 1 design for each size:

- Retângulo inline (300 X 250)
- Retângulo grande (336 x 280)
- Banner (468 x 60)
- Cabeçalho (728 x 90)

Please, find the briefing in pdf archive attached

Text we can work on th banners:

1 - Sofisticação com exclusividade para sua Casa!
2 - chique, exclusivo e encantador
3 - Encantador, sofisticado e exclusivo

The final image has to have Tessalvino´s Logo, Lar Ferreirinha´s logo and a call to action:

Confira nossos produtos exclusivos!

_________________________________________________________________
UPDATE

Please, for the colors, take the ones from pdf; (use more collors chics, silver and white, but not only this colors);
Don't forget the CALL TO ACTION " Confira nossos Produtos Exclusivos!"

If you'd like to meet the brand and the target, here is the page on Facebook: https://www.facebook.com/LarFerreirinhaHomeFerreirinha

But please, DO NOT COPY ANY OF THESE EXAMPLES ON THE PAGE.
We need something more executive.

Target Market(s)

Woman 30+
Trendy, modern, sofisticated, married or mum, cosmopolitan,
UPPERCLASS

Industry/Entity Type

Call

Font styles to use
Script
Other font styles liked:
• ColfaxTrial

Requirements
Must have
• Product images
Text
Product Image + Call to action on final layer with logos
As you will see the example in pdf archive attached
Nice to have
• frames
Should not have
• people
flowers
girlish drawing

```html
<!DOCTYPE html>
<html lang="pt-BR">
<head>
<meta charset="utf-8">
<title>Lar Ferreirinha – Banners</title>
<link rel="stylesheet" href="https://fonts.googleapis.com/css2?family=Rubik:ital,wght@0,400;1,700;1,800&display=swap">
<style>
  :root {
    --gutter: #ffffff;
    --headline-green: #2e6b33;
    --panel-green: #4fa862;
    --accent-pink: #e01a5a;
    --accent-pink-dark: #a80f40;
    --badge: #111111;
    --logo-grey: #8a8782;
    --logo-bar: rgba(255,255,255,0.82);
  }
  * { box-sizing: border-box; margin: 0; padding: 0; }
  html, body { width: 1200px; height: 1000px; overflow: hidden; background: var(--gutter); }
  .board {
    width: 1200px; height: 1000px;
    display: grid;
    grid-template-columns: 594px 594px;
    grid-template-rows: 494px 494px;
    gap: 12px;
    font-family: "Rubik", Arial, sans-serif;
  }
  .frame { position: relative; overflow: hidden; }
  .frame--white { background: #ffffff; }
  .frame--green { background: var(--panel-green); }
  .frame--room { background: #eef1f3; }

  .product-photo { position: absolute; }
  .product-photo--sheets {
    left: 26px; top: 196px; right: 0; bottom: 0;
    background: linear-gradient(172deg, #fdfdfd 0%, #eeeeef 30%, #f8f8f8 55%, #e4e5e7 80%, #d3d5d8 100%);
    border-top-left-radius: 30px 120px;
  }
  .product-photo--quilt {
    left: 232px; top: 168px; right: 0; bottom: 0;
    background: radial-gradient(ellipse at 55% 40%, #97a3d6 0%, #7583c0 45%, #56639f 80%, #48548c 100%);
    border-top-left-radius: 150px 140px;
  }
  .product-photo--bedroom {
    inset: 0;
    background: linear-gradient(180deg, #f5f7f8 0%, #eaeef1 35%, #dfe5ea 52%, #c5d1dd 60%, #6f8fb8 67%, #2f5b93 74%, #3d69a0 79%, #c9d3dd 85%, #eef0f2 91%, #e2e5e8 100%);
  }

  .headline {
    position: absolute; left: 24px; top: 20px; right: 16px;
    font-style: italic; font-weight: 800;
    font-size: 40px; line-height: 1.5;
  }
  .headline--green { color: var(--headline-green); }
  .headline--white { color: #ffffff; font-weight: 700; }
  .headline--pink { color: var(--accent-pink); top: 24px; line-height: 1.45; }

  .step-badge {
    position: absolute; left: 16px; bottom: 16px;
    width: 50px; height: 50px; border-radius: 50%;
    background: var(--badge); color: #ffffff;
    font-style: italic; font-weight: 800; font-size: 28px;
    display: flex; align-items: center; justify-content: center;
  }

  .brand-bar {
    position: absolute; left: 143px; right: 0; bottom: 0; height: 64px;
    background: var(--logo-bar);
    display: flex; align-items: center; justify-content: center;
  }
  .brand-name {
    font-family: "Rubik", Arial, sans-serif;
    font-weight: 400; font-size: 38px; letter-spacing: 2px;
    text-transform: uppercase; color: var(--logo-grey);
  }

  .cta-button {
    position: absolute; left: 89px; top: 208px; width: 419px; height: 138px;
    background: var(--accent-pink);
    border-radius: 10px;
    box-shadow: 0 7px 0 var(--accent-pink-dark);
    color: #ffffff; text-align: center;
    font-style: italic; font-weight: 700; font-size: 30px; line-height: 1.45;
    display: flex; align-items: center; justify-content: center;
  }
</style>
</head>
<body>
<main class="board">
  <section class="frame frame--white">
    <div class="product-photo product-photo--sheets" role="img" aria-label="Jogo de lençóis brancos dobrados com bordado de linhas escuras"></div>
    <h2 class="headline headline--green">Sofisticacai com<br>exclusividade para sua<br>Casa!</h2>
    <span class="step-badge">1</span>
    <div class="brand-bar"><span class="brand-name">Lar Ferreirinha</span></div>
  </section>

  <section class="frame frame--green">
    <div class="product-photo product-photo--quilt" role="img" aria-label="Colcha azul matelassê dobrada"></div>
    <h2 class="headline headline--white">Chique, exclusivo e<br>encantador</h2>
    <span class="step-badge">2</span>
    <div class="brand-bar"><span class="brand-name">Lar Ferreirinha</span></div>
  </section>

  <section class="frame frame--room">
    <div class="product-photo product-photo--bedroom" role="img" aria-label="Quarto claro com cama de cabeceira de ferro branca, roupa de cama branca e azul"></div>
    <h2 class="headline headline--pink">Encantador, sofisticado<br>e exclusivo!</h2>
    <span class="step-badge">3</span>
    <div class="brand-bar"><span class="brand-name">Lar Ferreirinha</span></div>
  </section>

  <section class="frame frame--room">
    <div class="product-photo product-photo--bedroom" role="img" aria-label="Quarto claro com cama de cabeceira de ferro branca, roupa de cama branca e azul"></div>
    <h2 class="headline headline--pink">Encantador, sofisticado<br>e exclusivo!</h2>
    <a class="cta-button">Confira Nossos<br>Produtos Exclusivos!</a>
    <span class="step-badge">4</span>
    <div class="brand-bar"><span class="brand-name">Lar Ferreirinha</span></div>
  </section>
</main>
</body>
</html>
```